Dental Office business/appointment cards
Bramble Cove Dental Clinic, Cosmetic, Implant and Family Dentistry
Creative Brief
Simple
Tom Hasselback BSc, DDS
Dr.
2817 Pelham Avenue Niagara Falls, Ontario L3K 4T9
bcdentalcare@quillpost.net
www.bramblecovedentalcare.net
I need an appointment card on the back with time and date spaces and the text "48 business hours notice required for cancellations"

```html
<!DOCTYPE html>
<html lang="en">
<head>
<meta charset="utf-8">
<title>Bramble Cove Dental Clinic – Stationery</title>
<link href="https://fonts.googleapis.com/css2?family=Montserrat:wght@400;600&display=swap" rel="stylesheet">
<style>
  :root{
    --bg:#e8e5e0;
    --paper:#ffffff;
    --blue:#29a3dd;
    --blue-deep:#1a86c2;
    --grey:#7c7e82;
    --grey-dark:#6a6c70;
    --grey-light:#c9cacc;
    --ink:#4a4c50;
    --shadow:0 2px 6px rgba(0,0,0,.18);
  }
  *{box-sizing:border-box;margin:0;padding:0}
  html,body{width:1200px;height:446px;overflow:hidden;background:var(--bg)}
  body{font-family:"Montserrat",Arial,sans-serif;color:var(--ink);position:relative}
  .piece{position:absolute;background:var(--paper);box-shadow:var(--shadow);overflow:hidden}
  .piece svg.art{position:absolute;left:0;width:100%}
  .brand{display:flex;align-items:center;gap:4px;color:var(--blue);font-weight:600;white-space:nowrap}
  .brand .dot{border-radius:50%;background:var(--blue);flex:none}

  /* business cards */
  .card-front{left:18px;top:166px;width:96px;height:58px}
  .card-front .brand{position:absolute;left:6px;top:12px;font-size:5px}
  .card-front .brand .dot{width:6px;height:6px}
  .card-front .details{position:absolute;left:6px;top:26px;font-size:3.2px;line-height:1.45;color:var(--grey)}
  .card-front .details .name{color:var(--ink);font-weight:600;font-size:3.6px}
  .card-front .art{bottom:0;height:14px}

  .card-back{left:18px;top:258px;width:96px;height:58px}
  .card-back .title{position:absolute;left:6px;top:6px;font-size:4px;font-weight:600;color:var(--blue)}
  .card-back .field{position:absolute;left:6px;font-size:3.4px;color:var(--grey);display:flex;align-items:flex-end;gap:3px;width:84px}
  .card-back .field span.line{flex:1;border-bottom:.5px solid var(--grey-light);height:4px}
  .card-back .note{position:absolute;left:6px;bottom:14px;font-size:2.9px;color:var(--ink)}
  .card-back .art{bottom:0;height:10px}

  /* letterheads */
  .letterhead{top:16px;height:412px}
  .letterhead-one{left:234px;width:222px}
  .letterhead-two{left:476px;width:290px}
  .letterhead .art.top{top:0;height:40px}
  .letterhead .art.bottom{bottom:0;height:90px}
  .letterhead .brand{position:absolute;left:16px;top:26px;font-size:7px}
  .letterhead .brand .dot{width:8px;height:8px}
  .letterhead .contact{position:absolute;right:14px;top:22px;font-size:3.6px;line-height:1.6;color:var(--grey);text-align:left}
  .letterhead-two .brand{left:44px;top:32px;font-size:8px}
  .letterhead-two .contact{right:22px;top:28px;font-size:4px}
  .letterhead-two .watermark{position:absolute;left:72px;top:128px;width:140px;height:140px;border-radius:50%;background:var(--blue);opacity:.08}

  /* envelopes */
  .envelope{left:826px;width:352px}
  .env-back-white{top:16px;height:92px}
  .env-back-grey{top:108px;height:92px;background:var(--grey)}
  .env-back-plain{top:214px;height:92px}
  .envelope .art{top:0;height:100%}
  .envelope .seal{position:absolute;left:50%;transform:translateX(-50%);width:10px;height:10px;border-radius:50%}
  .env-back-white .seal{top:22px;background:var(--grey-light)}
  .env-back-grey .seal{top:22px;background:var(--paper);opacity:.8}
  .env-back-plain .seal{top:42px;background:var(--blue)}
  .env-front{left:826px;top:320px;width:234px;height:108px}
  .env-front .brand{position:absolute;left:10px;top:10px;font-size:5.5px}
  .env-front .brand .dot{width:7px;height:7px}
  .env-front .art{bottom:0;height:34px}
</style>
</head>
<body>

<!-- Business card front -->
<section class="piece card-front" aria-label="Business card front">
  <div class="brand"><span class="dot"></span>Bramble Cove Dental Clinic</div>
  <div class="details">
    <div class="name">Dr. Tom Hasselback BSc, DDS</div>
    <div>2817 Pelham Avenue Niagara Falls, Ontario L3K 4T9</div>
    <div>bcdentalcare@quillpost.net</div>
    <div>www.bramblecovedentalcare.net</div>
  </div>
  <svg class="art" viewBox="0 0 100 14" preserveAspectRatio="none" aria-hidden="true">
    <path d="M0 6 C30 14 60 0 100 4 L100 14 L0 14Z" fill="var(--grey)"/>
    <path d="M0 9 C35 16 65 3 100 7 L100 14 L0 14Z" fill="var(--blue)"/>
  </svg>
</section>

<!-- Business card back / appointment -->
<section class="piece card-back" aria-label="Appointment card back">
  <div class="title">Appointment</div>
  <div class="field" style="top:16px">Date<span class="line"></span></div>
  <div class="field" style="top:25px">Time<span class="line"></span></div>
  <div class="note">48 business hours notice required for cancellations</div>
  <svg class="art" viewBox="0 0 100 10" preserveAspectRatio="none" aria-hidden="true">
    <path d="M0 4 C30 10 60 0 100 3 L100 10 L0 10Z" fill="var(--grey)"/>
    <path d="M0 6 C35 12 65 2 100 5 L100 10 L0 10Z" fill="var(--blue)"/>
  </svg>
</section>

<!-- Letterhead option 1 -->
<section class="piece letterhead letterhead-one" aria-label="Letterhead option 1">
  <svg class="art top" viewBox="0 0 100 18" preserveAspectRatio="none" aria-hidden="true">
    <path d="M0 0 L40 0 C20 3 8 8 0 16Z" fill="var(--blue)"/>
  </svg>
  <div class="brand"><span class="dot"></span>Bramble Cove Dental Clinic</div>
  <div class="contact">
    <div>2817 Pelham Avenue Niagara Falls,</div>
    <div>Ontario L3K 4T9</div>
    <div>bcdentalcare@quillpost.net</div>
    <div>www.bramblecovedentalcare.net</div>
  </div>
  <svg class="art bottom" viewBox="0 0 100 40" preserveAspectRatio="none" aria-hidden="true">
    <path d="M0 18 C30 34 65 6 100 10 L100 40 L0 40Z" fill="var(--grey)"/>
    <path d="M0 24 C32 40 66 12 100 16 L100 40 L0 40Z" fill="var(--blue)"/>
    <path d="M0 30 C35 44 70 20 100 24 L100 40 L0 40Z" fill="var(--blue-deep)" opacity=".35"/>
  </svg>
</section>

<!-- Letterhead option 2 -->
<section class="piece letterhead letterhead-two" aria-label="Letterhead option 2">
  <svg class="art top" viewBox="0 0 100 18" preserveAspectRatio="none" aria-hidden="true">
    <path d="M0 0 L100 0 L100 3 C70 10 30 2 0 12Z" fill="var(--grey-light)" opacity=".5"/>
  </svg>
  <div class="brand"><span class="dot"></span>Bramble Cove Dental Clinic</div>
  <div class="contact">
    <div>2817 Pelham Avenue Niagara Falls,</div>
    <div>Ontario L3K 4T9</div>
    <div>bcdentalcare@quillpost.net</div>
    <div>www.bramblecovedentalcare.net</div>
  </div>
  <div class="watermark" role="img" aria-label="Faint brand mark placeholder"></div>
  <svg class="art bottom" viewBox="0 0 100 40" preserveAspectRatio="none" aria-hidden="true">
    <path d="M0 16 C30 34 65 4 100 8 L100 40 L0 40Z" fill="var(--grey)"/>
    <path d="M0 22 C32 40 66 10 100 14 L100 40 L0 40Z" fill="var(--blue)"/>
  </svg>
</section>

<!-- Envelope backs -->
<section class="piece envelope env-back-white" aria-label="Envelope back, white">
  <svg class="art" viewBox="0 0 100 26" preserveAspectRatio="none" aria-hidden="true">
    <path d="M0 0 L100 0 L50 14Z" fill="var(--grey)"/>
    <path d="M0 26 L50 12 L100 26" fill="none" stroke="var(--grey-light)" stroke-width=".3"/>
  </svg>
  <span class="seal"></span>
</section>

<section class="piece envelope env-back-grey" aria-label="Envelope back, grey">
  <svg class="art" viewBox="0 0 100 26" preserveAspectRatio="none" aria-hidden="true">
    <path d="M0 0 L100 0 L50 14Z" fill="var(--grey-dark)"/>
    <path d="M0 26 L50 12 L100 26" fill="none" stroke="var(--grey-light)" stroke-width=".3"/>
  </svg>
  <span class="seal"></span>
</section>

<section class="piece envelope env-back-plain" aria-label="Envelope back, open flap">
  <svg class="art" viewBox="0 0 100 26" preserveAspectRatio="none" aria-hidden="true">
    <path d="M0 0 L50 10 L100 0" fill="none" stroke="var(--grey-light)" stroke-width=".3"/>
    <path d="M0 26 L50 14 L100 26" fill="none" stroke="var(--grey-light)" stroke-width=".3"/>
  </svg>
  <span class="seal"></span>
</section>

<!-- Envelope front -->
<section class="piece env-front" aria-label="Envelope front">
  <div class="brand"><span class="dot"></span>Bramble Cove Dental Clinic</div>
  <svg class="art" viewBox="0 0 100 16" preserveAspectRatio="none" aria-hidden="true">
    <path d="M0 6 C30 16 65 0 100 3 L100 16 L0 16Z" fill="var(--grey)"/>
    <path d="M0 9 C32 18 66 3 100 6 L100 16 L0 16Z" fill="var(--blue)"/>
  </svg>
</section>

</body>
</html>
```